Cellular Reward Program Flyer

We are launching a Customer Reward Program for our cellular retail business…. The marketing piece will be placed on our counter tops on high gloss cardstock or cardboard stand up type signs. I’m trying to keep this as clean and simple as possible. I found a few example’s of what I’d like to use as a basis.
Our biggest feature to our plan is our customers earn $20 every $100 spent. (requires 3 separate purchases)
No cards, no coupons, nothing needed.

our company logo is attached. you can also go to www.vornexa.com for other info on the company as we are a franchise

Industry/Entity Type

Marketing

```html
<!DOCTYPE html>
<html lang="en">
<head>
<meta charset="utf-8">
<title>Vornexa Customer Reward Flyer</title>
<link href="https://fonts.googleapis.com/css2?family=Roboto+Condensed:wght@700&family=Lato:wght@400;700&display=swap" rel="stylesheet">
<style>
  :root{
    --orange:#f0901f;
    --orange-deep:#e07a10;
    --orange-light:#ffb04a;
    --ink:#222222;
    --steel:#4a4a4a;
    --steel-dark:#2f2f2f;
    --paper:#ffffff;
    --mist:#ececec;
    --teal:#3fb7c4;
  }
  *{margin:0;padding:0;box-sizing:border-box}
  html,body{width:902px;height:1200px;overflow:hidden;background:var(--paper)}
  .flyer{position:relative;width:902px;height:1200px;overflow:hidden;
    background:radial-gradient(ellipse at 75% 45%, var(--mist) 0%, var(--paper) 60%);
    font-family:"Lato", Arial, sans-serif;color:var(--ink)}
  .flyer > *{position:absolute}
  .top-band{left:0;top:0;width:902px;height:260px}
  .headline{left:0;right:0;top:52px;text-align:center;white-space:nowrap;
    font-family:"Roboto Condensed", "Arial Narrow", sans-serif;font-weight:700;
    font-size:86px;line-height:1;color:var(--paper);letter-spacing:1px;
    text-shadow:0 3px 4px rgba(0,0,0,.35)}
  .big-rate{left:40px;top:200px;width:822px;text-align:center;white-space:nowrap;
    font-family:"Roboto Condensed", "Arial Narrow", sans-serif;font-weight:700;
    font-size:420px;line-height:1;letter-spacing:-4px;
    color:var(--steel);
    background:linear-gradient(180deg,#6a6a6a 0%,var(--steel) 45%,var(--steel-dark) 100%);
    -webkit-background-clip:text;background-clip:text;-webkit-text-fill-color:transparent;
    filter:drop-shadow(0 3px 2px rgba(0,0,0,.35))}
  .photo{left:420px;top:818px;width:480px;height:382px;
    border-radius:190px 190px 0 0;
    background:linear-gradient(180deg,#e9d3c3 0%,#d9b9a2 35%,var(--teal) 60%,#2c9aa7 100%)}
  .offer-ribbon{left:0;top:580px;width:840px;height:54px}
  .offer-text{left:60px;top:590px;
    font-family:"Roboto Condensed", "Arial Narrow", sans-serif;font-weight:700;
    font-size:26px;color:var(--paper);white-space:nowrap}
  .offer-text b{color:var(--ink)}
  .features-title{left:54px;top:650px;
    font-family:"Roboto Condensed", "Arial Narrow", sans-serif;font-weight:700;
    font-size:22px;color:var(--ink)}
  .feature{font-size:17px;font-weight:700;color:var(--ink);
    display:flex;align-items:center;gap:10px;white-space:nowrap}
  .feature svg{width:16px;height:16px}
  .feature-a{left:54px;top:688px}
  .feature-b{left:368px;top:688px}
  .feature-c{left:54px;top:724px}
  .points-line{left:58px;top:758px;font-size:19px;font-weight:700;white-space:nowrap}
  .points-line em{font-style:normal;color:var(--orange)}
  .footnote{left:398px;top:788px;font-size:10px;color:#555;white-space:nowrap}
  .brand{left:46px;top:832px;display:flex;align-items:center;gap:14px;
    font-family:"Lato", Arial, sans-serif;font-weight:400;font-size:56px;color:var(--steel)}
  .brand-dot{width:46px;height:46px;border-radius:50%;background:var(--orange)}
  .signup{left:52px;top:940px;width:256px;height:62px;border-radius:31px;
    background:linear-gradient(180deg,var(--orange-light) 0%,var(--orange) 50%,var(--orange-deep) 100%);
    box-shadow:0 3px 5px rgba(0,0,0,.3);display:flex;align-items:center;
    padding-left:32px;font-size:27px;font-weight:700;color:var(--paper);
    text-shadow:0 1px 2px rgba(0,0,0,.3)}
  .signup svg{position:absolute;right:10px;top:9px;width:44px;height:44px}
  .store-badge{left:59px;top:1034px;width:178px;height:55px;
    border-radius:8px;background:#1c1c1c;border:1px solid #777}
  .bottom-band{left:0;top:1112px;width:902px;height:88px;background:var(--orange)}
</style>
</head>
<body>
<main class="flyer">
  <svg class="top-band" viewBox="0 0 902 260" aria-hidden="true">
    <path d="M0 0 H902 V262 Q450 200 0 226 Z" fill="var(--orange)"/>
  </svg>
  <h1 class="headline">CUSTOMER EARNING</h1>
  <div class="big-rate">20%</div>

  <div class="bottom-band"></div>
  <div class="photo" role="img" aria-label="Photo of a smiling customer in a teal top holding up a smartphone and pointing at it"></div>

  <svg class="offer-ribbon" viewBox="0 0 840 54" aria-hidden="true">
    <path d="M0 0 H840 L812 27 L840 54 H0 Z" fill="var(--orange)"/>
  </svg>
  <p class="offer-text">Every <b>$100</b> in purchases automatically receive <b>$20.00</b> Store Credit</p>

  <h2 class="features-title">PROGRAM FEATURES</h2>
  <p class="feature feature-a"><svg viewBox="0 0 16 16"><path d="M2 8 L6 12 L14 3" fill="none" stroke="var(--orange)" stroke-width="3"/></svg>No Reward Cards To Keep</p>
  <p class="feature feature-b"><svg viewBox="0 0 16 16"><path d="M2 8 L6 12 L14 3" fill="none" stroke="var(--orange)" stroke-width="3"/></svg>No Receipts Needed For Warranties</p>
  <p class="feature feature-c"><svg viewBox="0 0 16 16"><path d="M2 8 L6 12 L14 3" fill="none" stroke="var(--orange)" stroke-width="3"/></svg>Store Credits Never Expire</p>
  <p class="points-line">Points Automatically Updated and Provided With <em>Every Purchase</em></p>
  <p class="footnote">*requires a minimum of 3 separate transactions on different dates</p>

  <div class="brand"><span class="brand-dot"></span>Vornexa</div>

  <div class="signup">Sign up now
    <svg viewBox="0 0 44 44" aria-hidden="true"><circle cx="22" cy="22" r="21" fill="#d9d9d9"/><path d="M17 12 L32 22 L17 32 Z" fill="#555"/></svg>
  </div>
  <div class="store-badge" role="img" aria-label="App store download badge"></div>
</main>
</body>
</html>
```